HomeBridle business card and stationary design

We are looking for a simple yet elegant design for our mortgage company business card and stationary.

The card should include:
Name (Derek Walsh)
Title (CEO)
Phone Number (614-208-3917)
Address (48 Birchfield Court, Suite 314, Marlow, OH 43952)
Email (email@homebridle-example.com)
"NMLS" i.e. (NMLS 61947)
"Company NMLS" (Company NMLS 472815)

See above

```html
<!DOCTYPE html>
<html lang="en">
<head>
<meta charset="utf-8">
<title>HomeBridle Business Card</title>
<link rel="stylesheet" href="https://fonts.googleapis.com/css2?family=Source+Sans+3:wght@400;600;700&display=swap">
<style>
  :root {
    --navy: #1a2330;
    --sky: #1fa3dc;
    --paper: #f4f4f4;
    --ink: #2a2f36;
    --rule: #8a8a8a;
    --backdrop: #e3e3e3;
    --white: #ffffff;
  }
  * { margin: 0; padding: 0; box-sizing: border-box; }
  html, body {
    width: 1200px; height: 960px; overflow: hidden;
    background: var(--backdrop);
    font-family: "Source Sans 3", "Source Sans Pro", sans-serif;
  }
  .card {
    position: absolute; left: 303px; width: 593px; height: 339px; overflow: hidden;
  }
  .card-front { top: 119px; background: var(--navy); }
  .card-back { top: 510px; background: var(--paper); }

  .brand-name {
    font-weight: 600; letter-spacing: 0.5px; white-space: nowrap; line-height: 1;
  }
  .card-front .brand-name {
    position: absolute; left: 0; right: 0; top: 146px; text-align: center;
    font-size: 72px; color: var(--white);
  }
  .tagline {
    position: absolute; left: 0; right: 0; top: 286px; text-align: center;
    font-size: 19px; color: var(--white);
  }
  .tagline strong { color: var(--sky); font-weight: 700; }

  .card-back .brand-name {
    position: absolute; left: 40px; top: 60px; font-size: 42px; color: var(--navy);
  }
  .person-name {
    position: absolute; right: 36px; top: 142px; font-size: 18px; font-weight: 700;
    color: var(--sky); letter-spacing: 0.3px;
  }
  .rule {
    position: absolute; left: 40px; top: 177px; width: 485px; height: 2px; background: var(--rule);
  }
  .person-title {
    position: absolute; right: 36px; top: 166px; font-size: 14px; color: var(--ink);
  }
  .address {
    position: absolute; left: 40px; top: 190px; font-size: 14.5px; line-height: 20px; color: var(--ink);
  }
  .contacts {
    position: absolute; left: 40px; top: 236px; list-style: none;
    font-size: 14.5px; line-height: 20px; color: var(--ink);
  }
  .contacts li { display: flex; align-items: center; gap: 5px; }
  .contacts svg { width: 13px; height: 13px; flex: none; }
  .footer-band {
    position: absolute; left: 0; bottom: 0; width: 100%; height: 30px;
  }
  .footer-band svg { position: absolute; inset: 0; }
  .company-nmls, .personal-nmls {
    position: absolute; top: 5px; font-size: 14px; color: var(--white);
  }
  .company-nmls { left: 40px; }
  .personal-nmls { right: 36px; }
</style>
</head>
<body>
  <section class="card card-front">
    <div class="brand-name">HomeBridle</div>
    <p class="tagline">Make yourself at home with <strong>HomeBridle</strong></p>
  </section>

  <section class="card card-back">
    <div class="brand-name">HomeBridle</div>
    <div class="person-name">DEREK WALSH</div>
    <div class="rule"></div>
    <div class="person-title">CEO</div>
    <address class="address" style="font-style:normal">
      48 Birchfield Court, Suite 314<br>Marlow, OH 43952
    </address>
    <ul class="contacts">
      <li>
        <svg viewBox="0 0 16 16" aria-hidden="true"><path d="M3.5 1.5l2.5 0 1 3.5-1.8 1.2a9 9 0 0 0 4.6 4.6L11 9l3.5 1v2.5c0 1-1 2-2 2A11 11 0 0 1 1.5 3.5c0-1 1-2 2-2z" fill="none" stroke="var(--sky)" stroke-width="1.6"/></svg>
        614-208-3917
      </li>
      <li>
        <svg viewBox="0 0 16 16" aria-hidden="true"><rect x="1.5" y="3.5" width="13" height="9" fill="none" stroke="var(--sky)" stroke-width="1.6"/><path d="M1.5 3.5l6.5 5 6.5-5" fill="none" stroke="var(--sky)" stroke-width="1.6"/></svg>
        email@homebridle-example.com
      </li>
      <li>
        <svg viewBox="0 0 16 16" aria-hidden="true"><circle cx="8" cy="8" r="6.3" fill="none" stroke="var(--sky)" stroke-width="1.4"/><ellipse cx="8" cy="8" rx="2.8" ry="6.3" fill="none" stroke="var(--sky)" stroke-width="1.2"/><path d="M1.7 8h12.6M2.8 4.8h10.4M2.8 11.2h10.4" stroke="var(--sky)" stroke-width="1.1"/></svg>
        www.homebridle.com
      </li>
    </ul>
    <div class="footer-band">
      <svg viewBox="0 0 593 30" width="593" height="30" aria-hidden="true">
        <rect width="593" height="30" fill="var(--navy)"/>
        <polygon points="426,30 436,0 440,0 430,30" fill="var(--white)"/>
        <polygon points="430,30 440,0 593,0 593,30" fill="var(--sky)"/>
      </svg>
      <span class="company-nmls">Company NMLS 472815</span>
      <span class="personal-nmls">NMLS 61947</span>
    </div>
  </section>
</body>
</html>
```